Business card design for Velvet Harbor

We need business cards designed for our new marketing consulting company, Velvet Harbor. Our services include marketing strategy, go-to-market and launch planning, growth strategy, and execution. We serve medical technology and health technology companies, from startups to well-established growth companies.

The business cards should feel professional, credible, reliable and trustworthy, and should instill confidence. Also bold, creative, and modern.

The design must use the Velvet Harbor logo.

The primary brand color is this orange: #FF5501
A secondary color that you can use is this gray: #282B2D
I would prefer only to use the orange and gray. But if you feel you really need an additional accent color (please use it very sparingly, as little as possible), you can use this blue for small accent purposes: #009FED

Attached are the logo files. The main logo is the one with a little bit of orange on the left and the rest is gray.

The business card should include the following:

Velvet Harbor logo
First name and last name
Title
Email address
Phone number and type (in whatever order looks best for the design
Website (the website does not need to be in the same block as the personal info)

For example:

Nessa Pryle
Founder & Principal
nessa@velvetharbor.com
+1.628.309.4156 mobile (can use "." or spaces in between blocks of numbers)
velvetharbor.com (somewhere on the card, it does not need to be with the personal info; and note that there is no "www." at the beginning)

Note that there will be no address listed on the business card.

Target Market(s)

Executives (CEO, head of marketing, head of sales) at medical technology and health technology companies, mostly in their 40s and older, well-educated, often with advanced degrees. They are strategic thinkers, responsible for budgets, and familiar with P&L. Their comfort with and trust in using outside consultants varies.

Industry/Entity Type

Medical technology and health technology companies.

Contact Information for Business Card

See project description

Font styles to use
Sans Serif

Requirements
Must have
• Logo and see Business card details section above.

```html
<!DOCTYPE html>
<html lang="en">
<head>
<meta charset="utf-8">
<title>Velvet Harbor — Business Card</title>
<link rel="stylesheet" href="https://fonts.googleapis.com/css2?family=Open+Sans:wght@400;600&display=swap">
<style>
  :root {
    --backdrop: #3d4d56;
    --card-light: #e3e6e7;
    --brand-orange: #e0672b;
    --brand-gray: #3a3f42;
    --ink-soft: #4a5053;
    --white: #f2f2f2;
  }
  * { box-sizing: border-box; margin: 0; padding: 0; }
  html, body { width: 1200px; height: 1200px; overflow: hidden; }
  body {
    background: var(--backdrop);
    font-family: "Open Sans", sans-serif;
    position: relative;
  }
  .card {
    position: absolute;
    left: 250px;
    width: 700px;
    height: 400px;
    border-radius: 4px;
    overflow: hidden;
  }
  .card--front { top: 150px; background: var(--card-light); color: var(--brand-gray); }
  .card--back { top: 650px; background: var(--brand-orange); }

  .holder { position: absolute; left: 70px; top: 118px; }
  .holder__name { font-size: 38px; font-weight: 400; letter-spacing: -0.5px; line-height: 1; }
  .holder__title { font-size: 14px; margin-top: 8px; color: var(--ink-soft); }

  .contact { position: absolute; left: 70px; bottom: 50px; display: flex; gap: 14px; }
  .contact__bar {
    width: 22px; background: var(--brand-orange);
    display: flex; flex-direction: column; justify-content: space-around; align-items: center;
    padding: 4px 0;
  }
  .contact__bar svg { width: 12px; height: 12px; }
  .contact__lines { font-size: 14px; line-height: 22px; color: var(--ink-soft); }

  .front-brand {
    position: absolute; right: 70px; top: 110px;
    font-size: 22px; font-weight: 600; letter-spacing: 3px; text-transform: uppercase;
    color: var(--brand-gray);
  }

  .back-brand {
    position: absolute; inset: 0;
    display: flex; align-items: center; justify-content: center; gap: 18px;
  }
  .back-brand__dot { width: 22px; height: 22px; border-radius: 50%; background: var(--white); }
  .back-brand__name {
    font-size: 30px; font-weight: 600; letter-spacing: 8px; text-transform: uppercase;
    color: var(--white);
  }
</style>
</head>
<body>
  <section class="card card--front">
    <div class="holder">
      <h1 class="holder__name">NESSA PRYLE</h1>
      <p class="holder__title">Founder &amp; Principal</p>
    </div>
    <div class="contact">
      <div class="contact__bar">
        <svg viewBox="0 0 12 12" aria-hidden="true"><path d="M2.5 1h2l1 3-1.3 1a6 6 0 0 0 2.8 2.8l1-1.3 3 1v2c0 .6-.4 1-1 1A9.5 9.5 0 0 1 1.5 2c0-.6.4-1 1-1z" fill="#fff"/></svg>
        <svg viewBox="0 0 12 12" aria-hidden="true"><rect x="1" y="2.5" width="10" height="7" fill="none" stroke="#fff" stroke-width="1.2"/><path d="M1 3l5 4 5-4" fill="none" stroke="#fff" stroke-width="1.2"/></svg>
        <svg viewBox="0 0 12 12" aria-hidden="true"><circle cx="6" cy="6" r="4.8" fill="none" stroke="#fff" stroke-width="1.1"/><ellipse cx="6" cy="6" rx="2" ry="4.8" fill="none" stroke="#fff" stroke-width="1"/><path d="M1.2 6h9.6" stroke="#fff" stroke-width="1"/></svg>
      </div>
      <div class="contact__lines">
        <p>+1.628.309.4156</p>
        <p>nessa@velvetharbor.com</p>
        <p>velvetharbor.com</p>
      </div>
    </div>
    <p class="front-brand">Velvet Harbor</p>
  </section>

  <section class="card card--back">
    <div class="back-brand">
      <span class="back-brand__dot"></span>
      <span class="back-brand__name">Velvet Harbor</span>
    </div>
  </section>
</body>
</html>
```